BrambleWorks business card

Looking for business card design that supports our company/software values. We have 2 logo designs at the moment but open to change if you think you can enhance the brand. Check out website www.brambleworks.com.au.

Target Market(s)

Education

Contact Information for Business Card

Name, title, mobile, email and website

Font styles to use
Sans Serif

Colors

Designer to choose colors to be used in the design.

Requirements
Must have
• BrambleWorks logo with tree and tagline on rear side with dark grey background colour

```html
<!DOCTYPE html>
<html lang="en">
<head>
<meta charset="utf-8">
<title>BrambleWorks business card</title>
<link rel="stylesheet" href="https://fonts.googleapis.com/css2?family=Open+Sans:wght@400;600;700&display=swap">
<style>
  :root {
    --canvas: #e6e6e6;
    --card-dark: #141414;
    --card-light: #ffffff;
    --brand-grey: #8f8f8f;
    --rule-grey: #6a6a6a;
    --accent: #f5a623;
    --accent-faint: #fdf1de;
    --text: #3c3c3c;
    --text-soft: #555555;
  }
  * { box-sizing: border-box; margin: 0; padding: 0; }
  html, body { width: 1200px; height: 960px; overflow: hidden; }
  body {
    background: var(--canvas);
    font-family: "Open Sans", sans-serif;
    position: relative;
  }
  .card {
    position: absolute;
    width: 580px;
    height: 331px;
    border-radius: 3px;
    box-shadow: 0 10px 28px rgba(0,0,0,0.18);
    overflow: hidden;
  }
  /* Rear side */
  .card--rear {
    left: 60px; top: 90px;
    background: var(--card-dark);
  }
  .rear-lockup {
    position: absolute;
    left: 150px; top: 112px;
    display: flex; align-items: center; gap: 22px;
  }
  .rear-lockup__mark {
    width: 64px; height: 64px; border-radius: 50%;
    background: #2a2a2a;
  }
  .rear-lockup__name {
    font-size: 46px; font-weight: 400; color: var(--brand-grey);
    line-height: 1; letter-spacing: 0.5px;
  }
  .rear-lockup__rule {
    height: 1px; background: var(--rule-grey); margin: 10px 0 6px;
  }
  .rear-lockup__tagline {
    font-size: 17px; color: var(--rule-grey); letter-spacing: 1px;
  }
  /* Front side */
  .card--front {
    left: 560px; top: 520px;
    background: var(--card-light);
  }
  .front-decor {
    position: absolute; right: -70px; top: -110px;
    width: 330px; height: 330px; border-radius: 50%;
    background: var(--accent-faint);
  }
  .contact {
    position: absolute; left: 40px; bottom: 34px;
  }
  .contact__name {
    font-size: 26px; font-weight: 700; color: var(--accent);
    letter-spacing: 1.5px; line-height: 1.1;
  }
  .contact__title {
    font-size: 17px; color: var(--text-soft); margin-top: 2px;
  }
  .contact__rule {
    width: 44px; height: 2px; background: var(--accent); margin: 10px 0 12px;
  }
  .contact__list { list-style: none; }
  .contact__item {
    display: flex; align-items: center; gap: 12px;
    font-size: 15px; color: var(--text); line-height: 1.6;
  }
  .contact__icon { width: 14px; height: 14px; flex: none; }
  .address {
    position: absolute; right: 34px; bottom: 40px;
    text-align: left; font-size: 15px; color: var(--text); line-height: 1.45;
  }
</style>
</head>
<body>
  <section class="card card--rear" aria-label="Card rear">
    <div class="rear-lockup">
      <span class="rear-lockup__mark"></span>
      <div class="rear-lockup__text">
        <div class="rear-lockup__name">BrambleWorks</div>
        <div class="rear-lockup__rule"></div>
        <div class="rear-lockup__tagline">Student Success Platform</div>
      </div>
    </div>
  </section>

  <section class="card card--front" aria-label="Card front">
    <div class="front-decor"></div>
    <div class="contact">
      <div class="contact__name">DANIEL REYES</div>
      <div class="contact__title">Founder &amp; CEO</div>
      <div class="contact__rule"></div>
      <ul class="contact__list">
        <li class="contact__item">
          <svg class="contact__icon" viewBox="0 0 14 14"><rect x="3" y="1" width="8" height="12" rx="1.5" fill="none" stroke="#f5a623" stroke-width="1.5"/><circle cx="7" cy="11" r="0.8" fill="#f5a623"/></svg>
          +61 400 287 314
        </li>
        <li class="contact__item">
          <svg class="contact__icon" viewBox="0 0 14 14"><path d="M3 1.5l2.5 2.5-1.3 1.6a8 8 0 0 0 4.2 4.2l1.6-1.3 2.5 2.5-1.7 1.7C6 12.5 1.5 8 1.3 3.2z" fill="#f5a623"/></svg>
          +61 2 8045 7731
        </li>
        <li class="contact__item">
          <svg class="contact__icon" viewBox="0 0 14 14"><rect x="1" y="3" width="12" height="8" rx="1" fill="#f5a623"/><path d="M1.5 3.5L7 8l5.5-4.5" fill="none" stroke="#fff" stroke-width="1.2"/></svg>
          hello@brambleworks.com.au
        </li>
        <li class="contact__item">
          <svg class="contact__icon" viewBox="0 0 14 14"><circle cx="7" cy="7" r="6" fill="#f5a623"/><path d="M1 7h12M7 1c-3 3-3 9 0 12M7 1c3 3 3 9 0 12" fill="none" stroke="#fff" stroke-width="0.9"/></svg>
          www.brambleworks.com.au
        </li>
      </ul>
    </div>
    <div class="address">
      410-225 Harbour Lane<br>
      Seaview, BC, V2K 4M8
    </div>
  </section>
</body>
</html>
```